Clarinet Past Midnight: mini recital & soiree

I need a poster design for a recital I'm doing next Friday April 25. It's an "after party" from 10 - 1am where I'll be playing a 30 min program followed by a DJ and there'll be food wine etc. I want to see a very "sexy" kind of poster. Modern with a "south beach" kind of art deco feel but without the really cheesy connotation that south beach sometimes has (if that makes any sense). I've included the link for the Facebook event so you can get an idea of the feel I want.

Cheers!

https://www.gatherloop.example/events/315907264810356/

Target Market(s)

College Students at the Coralwind State College

South Beach-ians

Industry/Entity Type

Events

Colors

Designer to choose colors to be used in the design.

Requirements
Must have
• Title of event..
Date..
Location..
Food / Beverage served..
DJ Verbosky..

```html
<!DOCTYPE html>
<html lang="en">
<head>
<meta charset="utf-8">
<title>Clarinet Past Midnight — Mini Recital &amp; Soiree</title>
<link rel="stylesheet" href="https://fonts.googleapis.com/css2?family=Oswald:wght@700&family=Open+Sans:wght@700&family=Roboto+Condensed:wght@700&family=Ultra&display=swap">
<style>
  :root {
    --backdrop: #0a1420;
    --band: #1d4f78;
    --frame: #ffffff;
    --ink: #050303;
    --ember: #b8290f;
    --flame: #e0701c;
    --glow: #f6c35a;
    --trail: #fff3d6;
    --badge: #ee1c1f;
    --white: #ffffff;
    --yellow: #f7e31b;
    --outline: #111111;
  }
  * { box-sizing: border-box; margin: 0; padding: 0; }
  html, body { width: 907px; height: 1200px; overflow: hidden; background: var(--backdrop); }
  .canvas {
    position: relative; width: 907px; height: 1200px;
    background:
      linear-gradient(to bottom, transparent 34%, rgba(29,79,120,.55) 36%, transparent 38%,
                      transparent 54%, rgba(29,79,120,.45) 56%, transparent 58%,
                      transparent 66%, rgba(29,79,120,.4) 68%, transparent 70%),
      var(--backdrop);
  }

  .poster {
    position: absolute; left: 109px; top: 53px; width: 699px; height: 1077px;
    border: 4px solid var(--frame); border-radius: 4px; overflow: hidden; background: var(--ink);
  }
  .poster__art {
    position: absolute; inset: 0;
    background:
      radial-gradient(ellipse 10% 30% at 48% 24%, rgba(255,243,214,.55), transparent 75%),
      radial-gradient(ellipse 30% 22% at 45% 14%, rgba(184,41,15,.55), transparent 75%),
      radial-gradient(ellipse 26% 30% at 44% 30%, rgba(246,195,90,.45), transparent 72%),
      radial-gradient(ellipse 34% 26% at 28% 52%, rgba(246,195,90,.45), transparent 72%),
      radial-gradient(ellipse 40% 42% at 22% 48%, rgba(224,112,28,.8), transparent 75%),
      radial-gradient(ellipse 30% 30% at 20% 68%, rgba(184,41,15,.75), transparent 75%),
      radial-gradient(ellipse 28% 30% at 14% 32%, rgba(184,41,15,.6), transparent 75%),
      radial-gradient(ellipse 70% 22% at 50% 86%, rgba(184,41,15,.8), transparent 75%),
      var(--ink);
  }
  .poster__crowd {
    position: absolute; left: 0; right: 0; bottom: 0; height: 150px;
    background: linear-gradient(to bottom, rgba(5,3,3,.2), var(--ink) 60%);
  }

  .date-badge {
    position: absolute; left: 451px; top: 94px; width: 218px; height: 218px;
    border-radius: 50%; background: var(--badge);
    display: flex; flex-direction: column; align-items: center; justify-content: center;
    font-family: "Roboto Condensed", "Arial Narrow", sans-serif; font-weight: 700;
    font-size: 42px; line-height: 1.2; text-align: center;
  }
  .date-badge__day { color: var(--white); }
  .date-badge__date { color: var(--ink); }

  .line {
    position: absolute; display: block; left: 158px; width: 540px; text-align: center; white-space: nowrap;
  }
  .tag {
    font-family: "Oswald", Impact, sans-serif; font-weight: 700; color: var(--yellow);
    text-shadow: -2px -2px 0 var(--outline), 2px -2px 0 var(--outline),
                 -2px 2px 0 var(--outline), 2px 2px 0 var(--outline),
                 0 2px 0 var(--outline), 0 -2px 0 var(--outline),
                 2px 0 0 var(--outline), -2px 0 0 var(--outline);
  }
  .tag--dj { top: 329px; left: 381px; width: 300px; font-size: 32px; line-height: 40px; }
  .tag--kind { top: 664px; font-size: 44px; line-height: 52px; }
  .tag--fare { top: 935px; font-size: 26px; line-height: 34px; }

  .title { color: var(--white); }
  .title--lead {
    top: 378px; font-family: "Roboto Condensed", "Arial Narrow", sans-serif; font-weight: 700;
    font-size: 118px; line-height: 118px;
  }
  .title--link {
    top: 512px; font-family: "Open Sans", Arial, sans-serif; font-weight: 700;
    font-size: 42px; line-height: 50px;
  }
  .title--close {
    top: 570px; font-family: "Ultra", "Rockwell Extra Bold", Georgia, serif; font-weight: 400;
    font-size: 60px; line-height: 70px; letter-spacing: 2px;
  }

  .details { font-family: "Open Sans", Arial, sans-serif; font-weight: 700; color: var(--white); }
  .details--time { top: 750px; font-size: 36px; line-height: 46px; }
  .details--zone { top: 812px; font-size: 36px; line-height: 46px; }
  .details--venue {
    top: 879px; font-family: "Roboto Condensed", "Arial Narrow", sans-serif;
    font-size: 38px; line-height: 46px;
  }
</style>
</head>
<body>
<main class="canvas">
  <section class="poster">
    <div class="poster__art" role="img" aria-label="Illustration of glowing red and white light trails swirling over a clarinet and flame-like flourishes"></div>
    <div class="poster__crowd" role="img" aria-label="Silhouetted crowd with raised hands against a red glow"></div>

    <div class="date-badge">
      <span class="date-badge__day">FRIDAY,</span>
      <span class="date-badge__date">APRIL 25</span>
    </div>

    <p class="line tag tag--dj">DJ VERBOSKY</p>
    <h1>
      <span class="line title title--lead">CLARINET</span>
      <span class="line title title--link">PAST</span>
      <span class="line title title--close">MIDNIGHT</span>
    </h1>
    <p class="line tag tag--kind">MINI RECITAL &amp; SOIREE</p>
    <p class="line details details--time">AT 10:00PM - 1:00AM</p>
    <p class="line details details--zone">IN EDT</p>
    <p class="line details details--venue">HARLOW COMMONS HALL</p>
    <p class="line tag tag--fare">FOOD &amp; WINE SERVED</p>
  </section>
</main>
</body>
</html>
```